Moder Business Card Design for Renewables Business

Need a business card design for my business. We collect & repurpose spent coffee ground from cafes. The cards will be made from recycled paper. Needs to fit our corporate colour scheme of white, green & brown (see logo for colour codes). Eco friendly, modern, intresting & eye catching.
This card needs to convey the message of the business and fit into its mantra of eco-friendly, sustainable etc.

Target Market(s)

Cafe Owners, Coffee Drinkers, Recycling Companies, Farmers

Industry/Entity Type

Recycling

Contact Information for Business Card

Name; Peter Halloran
Phone; 0412 386 527
e-mail; info@lumatrove.com.au
website; www.lumatrove.com.au

Font styles to use
Sans Serif
Script

Colors

Designer to choose colors to be used in the design.

Requirements
Must have
• FRONT;
• Logo, Name (Peter Halloran), phone number, e-mail address, website
• BACK;
• On the back in cursive text; 'GREENER GROUNDS FOR EVERY SINGLE CUP'
• Small facebook & Instagram logos with text 'Lumatrove'
Should not have
• messy design

```html
<!DOCTYPE html>
<html lang="en">
<head>
<meta charset="utf-8">
<title>Lumatrove Business Card</title>
<link rel="stylesheet" href="https://fonts.googleapis.com/css2?family=Dancing+Script:wght@700&family=Source+Sans+3:wght@400;600&display=swap">
<style>
  :root {
    --backdrop: #e7e4de;
    --paper: #f8f7f3;
    --green: #7ab648;
    --brown: #7a5036;
    --grey: #55565a;
    --shadow: rgba(60, 45, 30, 0.18);
  }
  * { box-sizing: border-box; margin: 0; padding: 0; }
  html, body {
    width: 1200px;
    height: 918px;
    overflow: hidden;
    background: var(--backdrop);
  }
  .canvas {
    position: relative;
    width: 1200px;
    height: 918px;
  }
  .card {
    position: absolute;
    left: 250px;
    width: 700px;
    height: 400px;
    background: var(--paper);
    box-shadow: 0 6px 18px var(--shadow);
    font-family: "Source Sans 3", "Myriad Pro", sans-serif;
  }
  .card--back { top: 39px; }
  .card--front { top: 479px; }

  /* Brand lockup */
  .brand {
    position: absolute;
    display: flex;
    flex-direction: column;
    align-items: center;
  }
  .brand__mark { display: block; }
  .brand__name {
    margin-top: 10px;
    font-weight: 400;
    letter-spacing: 1px;
    text-transform: uppercase;
    line-height: 1;
  }

  /* Back */
  .card--back .brand {
    left: 0;
    right: 0;
    top: 34px;
  }
  .card--back .brand__name {
    color: var(--brown);
    font-size: 30px;
  }
  .tagline {
    position: absolute;
    left: 0;
    right: 0;
    top: 198px;
    text-align: center;
    font-family: "Dancing Script", cursive;
    font-weight: 700;
    font-size: 50px;
    line-height: 1;
    color: var(--brown);
  }
  .socials {
    position: absolute;
    left: 70px;
    right: 70px;
    top: 290px;
    display: flex;
    justify-content: space-between;
    align-items: flex-start;
  }
  .social {
    display: flex;
    align-items: center;
    gap: 8px;
    color: var(--grey);
    font-size: 26px;
    line-height: 1;
  }
  .social__dot {
    width: 18px;
    height: 18px;
    border-radius: 50%;
    background: var(--grey);
    flex: none;
  }
  .back-web {
    position: absolute;
    left: 70px;
    top: 332px;
    color: var(--green);
    font-size: 22px;
  }

  /* Front */
  .card--front .brand {
    left: 60px;
    width: 240px;
    top: 78px;
  }
  .card--front .brand__name {
    color: var(--green);
    font-size: 34px;
    margin-top: 14px;
  }
  .divider {
    position: absolute;
    left: 340px;
    top: 90px;
    width: 4px;
    height: 220px;
    background: var(--green);
  }
  .contact {
    position: absolute;
    left: 370px;
    right: 20px;
    top: 120px;
    text-align: center;
    color: var(--brown);
    font-size: 27px;
    line-height: 33px;
    font-style: normal;
  }
</style>
</head>
<body>
<main class="canvas">

  <section class="card card--back" aria-label="Card back">
    <div class="brand">
      <svg class="brand__mark" width="110" height="110" viewBox="0 0 110 110" aria-hidden="true">
        <circle cx="55" cy="55" r="50" fill="none" stroke="var(--brown)" stroke-width="5"/>
      </svg>
      <span class="brand__name">Lumatrove</span>
    </div>
    <p class="tagline">Greener grounds for every single cup</p>
    <div class="socials">
      <span class="social"><span class="social__dot"></span>lumatrove</span>
      <span class="social"><span class="social__dot"></span>lumatrove</span>
    </div>
    <span class="back-web">www.lumatrove.com.au</span>
  </section>

  <section class="card card--front" aria-label="Card front">
    <div class="brand">
      <svg class="brand__mark" width="140" height="140" viewBox="0 0 140 140" aria-hidden="true">
        <circle cx="70" cy="70" r="64" fill="none" stroke="var(--brown)" stroke-width="6"/>
      </svg>
      <span class="brand__name">Lumatrove</span>
    </div>
    <span class="divider"></span>
    <address class="contact">
      Peter Halloran<br>
      0412 386 527<br>
      info@lumatrove.com.au<br>
      www.lumatrove.com.au<br>
      www.lumatrove.com.au
    </address>
  </section>

</main>
</body>
</html>
```